Business cards for Brightmarrow Consulting with the following info for the front side:

Brightmarrow Consulting
Executive Coaching and Human Capital Strategy
www.brightmarrow.example

Lorena Vaduvic
Principal
lorena@brightmarrow.example
+1 604 555 0172

Black background, text using the colours of the logo - enclosed.

The back side of the business card should feature the logo in the middle, with "Executive Coaching and Human Capital Strategy" on top and "www.brightmarrow.example" below.

```html
<!DOCTYPE html>
<html lang="en">
<head>
<meta charset="utf-8">
<title>Brightmarrow Consulting — Business Cards</title>
<link href="https://fonts.googleapis.com/css2?family=Montserrat:wght@400;500;600;700&display=swap" rel="stylesheet">
<style>
  :root {
    --stage: #3b3b3b;
    --card: #060606;
    --pattern: #151515;
    --blue: #1f9fc9;
    --yellow: #f2b51b;
    --white: #f2f2f2;
    --rule: #cfcfcf;
  }
  * { box-sizing: border-box; margin: 0; padding: 0; }
  html, body { width: 1200px; height: 1021px; overflow: hidden; }
  body {
    background: var(--stage);
    font-family: "Montserrat", Arial, sans-serif;
    position: relative;
  }
  .card {
    position: absolute;
    left: 230px;
    width: 740px;
    height: 423px;
    background: var(--card);
    border-radius: 4px;
    box-shadow: 0 10px 30px rgba(0,0,0,.45);
    overflow: hidden;
  }
  .card--back { top: 50px; }
  .card--front { top: 523px; }

  /* back */
  .back-pattern {
    position: absolute; inset: 0;
    background: radial-gradient(ellipse at center, #1b1b1b 0%, var(--pattern) 70%);
  }
  .back-content {
    position: absolute; inset: 0;
    display: flex; flex-direction: column; align-items: center; justify-content: center;
  }
  .brand {
    display: flex; align-items: center; gap: 18px;
  }
  .brand__dot {
    border-radius: 50%;
    border: 4px solid var(--yellow);
  }
  .brand__name {
    font-weight: 600;
    color: var(--blue);
    letter-spacing: 2px;
  }
  .card--back .brand__dot { width: 74px; height: 74px; }
  .card--back .brand__name { font-size: 48px; }
  .back-tagline {
    margin-top: 30px;
    color: var(--white);
    font-size: 17px;
    letter-spacing: .5px;
  }
  .back-url {
    margin-top: 14px;
    color: var(--blue);
    font-size: 16px;
  }
  .accent { color: var(--yellow); }

  /* front */
  .card--front .brand {
    position: absolute; left: 40px; top: 40px;
  }
  .card--front .brand__dot { width: 80px; height: 80px; }
  .card--front .brand__name { font-size: 52px; }
  .person {
    position: absolute; left: 46px; top: 225px;
  }
  .person__name {
    color: var(--blue); font-weight: 700; font-size: 24px;
  }
  .person__role {
    color: var(--white); font-size: 18px; margin-top: 2px;
  }
  .divider {
    position: absolute; left: 365px; top: 215px;
    width: 1px; height: 160px; background: var(--rule);
  }
  .details {
    position: absolute; left: 398px; top: 222px;
    color: var(--white); font-size: 18px; line-height: 1.35;
  }
  .details__company { color: var(--blue); font-weight: 500; }
  .details__services { margin-bottom: 8px; }
  .contact { list-style: none; }
  .contact li { display: flex; align-items: center; gap: 10px; }
  .contact svg { width: 18px; height: 18px; flex: none; }
</style>
</head>
<body>

<section class="card card--back" aria-label="Card back">
  <div class="back-pattern" role="img" aria-label="Faint repeating pattern of circular emblems across the card"></div>
  <div class="back-content">
    <div class="brand">
      <span class="brand__dot"></span>
      <span class="brand__name">BRIGHTMARROW</span>
    </div>
    <p class="back-tagline">Executive Coaching &amp; Human Capital Strategy</p>
    <p class="back-url">www.<span class="accent">brightmarrow</span>.example</p>
  </div>
</section>

<section class="card card--front" aria-label="Card front">
  <div class="brand">
    <span class="brand__dot"></span>
    <span class="brand__name">BRIGHTMARROW</span>
  </div>

  <div class="person">
    <p class="person__name">Lorena Vaduvic</p>
    <p class="person__role">Principal</p>
  </div>

  <div class="divider"></div>

  <div class="details">
    <p class="details__company">Brightmarrow <span class="accent">Consulting</span></p>
    <p class="details__services">Executive Coaching &amp;<br>Human Capital Strategy</p>
    <ul class="contact">
      <li>
        <svg viewBox="0 0 24 24" aria-hidden="true"><path fill="#f2b51b" d="M6.6 10.8a15 15 0 0 0 6.6 6.6l2.2-2.2c.3-.3.7-.4 1-.2 1.1.4 2.3.6 3.6.6.6 0 1 .4 1 1V20c0 .6-.4 1-1 1A17 17 0 0 1 3 4c0-.6.4-1 1-1h3.5c.6 0 1 .4 1 1 0 1.3.2 2.5.6 3.6.1.3 0 .7-.2 1z"/></svg>
        +1 604 555 0172
      </li>
      <li>
        <svg viewBox="0 0 24 24" aria-hidden="true"><rect x="2.5" y="5" width="19" height="14" fill="none" stroke="#f2b51b" stroke-width="2"/><path d="M3 6l9 7 9-7" fill="none" stroke="#f2b51b" stroke-width="2"/></svg>
        lorena@brightmarrow.example
      </li>
      <li>
        <svg viewBox="0 0 24 24" aria-hidden="true"><g fill="none" stroke="#f2b51b" stroke-width="1.8"><circle cx="12" cy="12" r="9.5"/><ellipse cx="12" cy="12" rx="4.5" ry="9.5"/><path d="M2.5 12h19M4 7h16M4 17h16"/></g></svg>
        www.brightmarrow.example
      </li>
    </ul>
  </div>
</section>

</body>
</html>
```